Business card for event manager / organizer "velmora tandem"

Draft of a new valuable business card for my company.
Events, personnel service providers, festivals

```html
<!DOCTYPE html>
<html lang="de">
<head>
<meta charset="utf-8">
<title>Velmora Tandem – Visitenkarte</title>
<link href="https://fonts.googleapis.com/css2?family=Source+Sans+3:wght@300;600;700&display=swap" rel="stylesheet">
<style>
  :root {
    --backdrop: #6e6f73;
    --card-black: #050505;
    --panel-black: #0b0c10;
    --gold: #a08a6c;
    --gold-light: #b9a17f;
    --white: #ffffff;
    --ink: #222222;
  }
  * { margin: 0; padding: 0; box-sizing: border-box; }
  html, body { width: 1200px; height: 1200px; overflow: hidden; }
  body {
    background: var(--backdrop);
    font-family: "Source Sans 3", "Segoe UI", sans-serif;
    position: relative;
  }
  .card {
    position: absolute;
    left: 220px;
    width: 760px;
    height: 432px;
    border-radius: 30px;
    overflow: hidden;
    background: var(--card-black);
  }
  .card--front { top: 104px; }
  .card--back { top: 652px; }

  /* Brand block */
  .brand { display: flex; align-items: center; }
  .brand__square { background: var(--gold); flex: none; }
  .brand__text { display: flex; flex-direction: column; }
  .brand__name {
    color: var(--white);
    font-weight: 700;
    text-transform: uppercase;
    line-height: 0.95;
  }
  .brand__tagline {
    color: var(--gold-light);
    font-weight: 300;
    white-space: nowrap;
  }

  /* Front */
  .front__panel {
    position: absolute;
    left: 168px; top: 72px;
    width: 422px; height: 274px;
    background: var(--panel-black);
    display: flex;
    align-items: center;
    justify-content: center;
  }
  .brand--large { gap: 18px; }
  .brand--large .brand__square { width: 66px; height: 66px; }
  .brand--large .brand__name { font-size: 42px; letter-spacing: 1px; }
  .brand--large .brand__tagline { font-size: 14px; margin-top: 8px; }
  .front__url {
    position: absolute;
    left: 0; right: 0; top: 394px;
    text-align: center;
    color: var(--gold);
    font-weight: 700;
    font-size: 16px;
    letter-spacing: 3.5px;
  }

  /* Back */
  .back__photo { position: absolute; left: 0; top: 0; }
  .back__tab {
    position: absolute;
    left: 0; top: 36px;
    width: 128px; height: 28px;
    background: #1a1718;
    border-radius: 0 28px 0 0;
  }
  .back__band {
    position: absolute;
    left: 0; bottom: 0;
    width: 100%; height: 40px;
    background: var(--gold);
  }
  .portrait { position: absolute; left: 44px; top: 92px; }
  .person {
    position: absolute;
    left: 0; width: 312px; top: 300px;
    text-align: center;
  }
  .person__name {
    color: var(--ink);
    font-weight: 700;
    font-size: 22px;
    line-height: 1;
  }
  .person__role {
    display: inline-block;
    margin-top: 4px;
    color: var(--gold);
    font-weight: 700;
    font-size: 15px;
    letter-spacing: 3.5px;
    padding-bottom: 2px;
    border-bottom: 2px solid var(--gold);
  }
  .back__logo-box {
    position: absolute;
    left: 544px; top: 34px;
    width: 194px; height: 100px;
    background: var(--panel-black);
    display: flex;
    align-items: center;
    justify-content: center;
  }
  .brand--small { gap: 8px; }
  .brand--small .brand__square { width: 32px; height: 32px; }
  .brand--small .brand__name { font-size: 20px; }
  .brand--small .brand__tagline { font-size: 7px; margin-top: 3px; }

  .contact-icons { position: absolute; left: 296px; top: 0; }
  .contact {
    position: absolute;
    left: 354px;
    color: var(--gold-light);
    font-weight: 700;
    font-size: 14.5px;
    line-height: 13px;
    text-transform: uppercase;
    list-style: none;
  }
  .contact li { position: absolute; left: 0; white-space: nowrap; }
  .contact__city { display: inline-block; margin-top: 5px; }
</style>
</head>
<body>

<section class="card card--front" aria-label="Visitenkarte Vorderseite">
  <div class="front__panel">
    <div class="brand brand--large">
      <span class="brand__square"></span>
      <div class="brand__text">
        <span class="brand__name">Velmora<br>Tandem</span>
        <span class="brand__tagline">…weil jedes Event einen Plan braucht!</span>
      </div>
    </div>
  </div>
  <p class="front__url">WWW.VELMORA-TANDEM.DE</p>
</section>

<section class="card card--back" aria-label="Visitenkarte Rückseite">
  <svg class="back__photo" width="340" height="392" viewBox="0 0 340 392" role="img" aria-label="Konzertfoto mit Publikum und Bühnenlicht">
    <defs>
      <linearGradient id="crowdTone" x1="0" y1="0" x2="0" y2="1">
        <stop offset="0" stop-color="#ece4f2"/>
        <stop offset="0.45" stop-color="#d8d0de"/>
        <stop offset="1" stop-color="#cfcbd1"/>
      </linearGradient>
    </defs>
    <path d="M0 0 H295 V86 H310 A30 30 0 0 1 340 116 V320 A30 30 0 0 1 310 350 H295 V392 H0 Z" fill="url(#crowdTone)"/>
  </svg>
  <div class="back__tab"></div>

  <svg class="portrait" width="196" height="196" viewBox="0 0 196 196" role="img" aria-label="Porträtfoto des Inhabers">
    <defs>
      <radialGradient id="portraitTone" cx="0.5" cy="0.4" r="0.6">
        <stop offset="0" stop-color="#8a8a8c"/>
        <stop offset="1" stop-color="#2e2e30"/>
      </radialGradient>
    </defs>
    <circle cx="98" cy="98" r="95" fill="url(#portraitTone)" stroke="#a08a6c" stroke-width="4"/>
  </svg>

  <div class="person">
    <p class="person__name">ARNE FELDKAMP</p>
    <p class="person__role">INHABER</p>
  </div>

  <div class="back__logo-box">
    <div class="brand brand--small">
      <span class="brand__square"></span>
      <div class="brand__text">
        <span class="brand__name">Velmora<br>Tandem</span>
        <span class="brand__tagline">…weil jedes Event einen Plan braucht!</span>
      </div>
    </div>
  </div>

  <svg class="contact-icons" width="30" height="340" viewBox="0 0 30 340" fill="none" stroke="#a08a6c" stroke-width="1.6" aria-hidden="true">
    <circle cx="15" cy="146" r="14"/>
    <path d="M10 140 l3 -2 l2 4 l-2 1.5 q1.5 3.5 4.5 5 l1.5 -2 l4 2 l-2 3 q-9 -1 -11 -11.5z" fill="#a08a6c" stroke="none"/>
    <circle cx="15" cy="185" r="14"/>
    <circle cx="15" cy="185" r="8"/>
    <path d="M7 185 H23 M15 177 V193 M15 177 q-5 8 0 16 M15 177 q5 8 0 16"/>
    <circle cx="15" cy="224" r="14"/>
    <rect x="8" y="219" width="14" height="10" fill="#a08a6c" stroke="none"/>
    <path d="M8 219 l7 6 l7 -6" stroke="#050505" stroke-width="1.2"/>
    <circle cx="15" cy="263" r="14"/>
    <path d="M7 263 l8 -7 l8 7 h-2.5 v7 h-11 v-7z" fill="#a08a6c" stroke="none"/>
    <circle cx="15" cy="302" r="14"/>
  </svg>

  <ul class="contact">
    <li style="top:133px">0231 555 24 18<br>0170 555 73 42</li>
    <li style="top:179px">WWW.VELMORA-TANDEM.DE</li>
    <li style="top:218px">INFO@VELMORA-TANDEM.DE</li>
    <li style="top:248px">BIRKENHOF 12, 40210<br><span class="contact__city">NEUSTADT</span></li>
    <li style="top:296px">WWW.VELMORA-TANDEM.DE/EVENTS</li>
  </ul>

  <div class="back__band"></div>
</section>

</body>
</html>
```